Einladungskarten für Der Helle Bogen
Designer hat mehrere Vorschläge entwickelt und Änderungen super schnell umgesetzt. Wir waren sehr zufrieden und freuen uns auf unsere diesjährige Einladungskarte.
Zielgruppe
Wir sind ein Tochterunternehmen von Harting Verlag. Wir sind 'Der Helle Bogen' , Holding der Radio Stationen/Beteiligungen und möchten alle Geschäftsführer/innen der Beteiligungen, einige Politiker und Medienräte zu einem Event einladen.
Aufgabenstellung
Wir hätten gerne eine quadratische Karte.
Das Event heißt 'Ortsabend 2023'
Termin 03.07.2023 um 19 Uhr
Anmeldung bis spätestens 23.06.2022 an events@heller-bogen.de
Diese Karte gilt als Eintrittskarte
Adresse: KAIHALLE, Lindenweg 52, 90461 Nürnberg
Dresscode: Business Casual
Firmenfarben: Blau: RGB 23/110/182 und Grau: RGB 134/135/135
Firmenschriftart: Century Gothic

```html
<!DOCTYPE html>
<html lang="de">
<head>
<meta charset="utf-8">
<title>Ortsabend 2023 – Einladung</title>
<link rel="stylesheet" href="https://fonts.googleapis.com/css2?family=Questrial&family=Roboto:wght@700;900&family=Mulish:wght@800&display=swap">
<style>
  :root {
    --brand-blue: #176eb6;
    --brand-grey: #868787;
    --paper: #ffffff;
    --photo-light: #c9d6cf;
    --photo-dark: #5f7a4e;
  }
  html, body {
    margin: 0;
    padding: 0;
    width: 1200px;
    height: 1200px;
    overflow: hidden;
    background: var(--paper);
  }
  .card {
    position: relative;
    width: 1200px;
    height: 1200px;
    overflow: hidden;
    background: var(--paper);
    font-family: "Questrial", "Century Gothic", sans-serif;
    color: var(--paper);
  }
  .top-band {
    position: absolute;
    left: 0; top: 0;
    width: 1052px; height: 30px;
    background: var(--brand-blue);
  }
  .event-title {
    position: absolute;
    left: 88px; top: 52px;
    margin: 0;
    font-weight: 400;
    font-size: 134px;
    line-height: 1;
    letter-spacing: 1px;
    color: var(--brand-blue);
  }
  .event-mark {
    position: absolute;
    left: 990px; top: 62px;
    width: 98px; height: 98px;
    border-radius: 50%;
    background: var(--brand-grey);
  }
  .info-panel {
    position: absolute;
    left: 0; top: 205px;
    width: 1052px; height: 995px;
    background: var(--brand-blue);
  }
  .event-date {
    position: absolute;
    left: 70px; top: 262px;
    margin: 0;
    font-family: "Roboto", Arial, sans-serif;
    font-weight: 900;
    font-size: 108px;
    line-height: 1;
    letter-spacing: -1px;
  }
  .dresscode {
    position: absolute;
    left: 72px; top: 398px;
    margin: 0;
    font-size: 50px;
    line-height: 1;
  }
  .dresscode strong {
    font-family: "Mulish", "Century Gothic", sans-serif;
    font-weight: 800;
  }
  .venue {
    position: absolute;
    left: 72px; top: 512px;
    margin: 0;
    font-style: normal;
    font-size: 52px;
    line-height: 58px;
  }
  .registration {
    position: absolute;
    left: 72px; top: 798px;
    margin: 0;
    font-size: 30px;
    line-height: 37px;
  }
  .ticket-note {
    position: absolute;
    left: 72px; top: 906px;
    margin: 0;
    font-size: 30px;
    line-height: 1;
  }
  .divider {
    position: absolute;
    left: 0; top: 970px;
    width: 670px; height: 7px;
    background: var(--brand-grey);
  }
  .divider-post {
    position: absolute;
    left: 630px; top: 780px;
    width: 22px; height: 420px;
    border-radius: 11px 11px 0 0;
    background: var(--brand-grey);
  }
  .host-name {
    position: absolute;
    left: 70px; top: 1015px;
    margin: 0;
    font-size: 54px;
    line-height: 1;
    letter-spacing: 1px;
  }
  .host-square {
    position: absolute;
    left: 72px; top: 1096px;
    width: 22px; height: 22px;
    background: var(--brand-grey);
  }
  .photo-frame-back {
    position: absolute;
    left: 712px; top: 730px;
    width: 468px; height: 500px;
    border: 12px solid var(--brand-grey);
    border-radius: 22px;
    box-sizing: border-box;
  }
  .photo-frame {
    position: absolute;
    left: 670px; top: 698px;
    width: 484px; height: 520px;
    padding: 22px;
    box-sizing: border-box;
    border-radius: 22px;
    background: var(--paper);
  }
  .photo {
    width: 100%;
    height: 100%;
    border-radius: 6px;
    background: linear-gradient(170deg, var(--photo-dark) 0%, var(--photo-light) 55%, #8f9a8c 100%);
  }
</style>
</head>
<body>
  <main class="card">
    <div class="top-band"></div>
    <h1 class="event-title">ORTSABEND</h1>
    <div class="event-mark"></div>

    <section class="info-panel"></section>

    <p class="event-date">03.07.2023 19 Uhr</p>
    <p class="dresscode">Dresscode: <strong>Business Casual</strong></p>
    <address class="venue">KAIHALLE,<br>Lindenweg 52,<br>90461 Nürnberg</address>

    <p class="registration">Anmeldung bis spätestens 23.06.2023<br>an events@heller-bogen.de</p>
    <p class="ticket-note">Diese Karte gilt als Eintrittskarte</p>

    <div class="divider-post"></div>
    <div class="divider"></div>

    <p class="host-name">DER HELLE BOGEN</p>
    <div class="host-square"></div>

    <div class="photo-frame-back"></div>
    <div class="photo-frame">
      <div class="photo" role="img" aria-label="Foto der Terrasse am See mit Tischen, Stühlen und Sonnenschirm im Grünen"></div>
    </div>
  </main>
</body>
</html>
```